Orthopaedic Clinic Needs facebook page

Orthopaedic Clinic needs facebook page. The name of our clinic is Larchmont Orthopaedics. We focus on hip and knee orthopaedic conditions, as well as general orthopaedics. The main services are total knee replacements, total hip replacements, sports injury of the knee, hip fractures. Unique selling points of our service would be 1. Patient Centred Care, 2. Value Driven, 3. 2 Double-Fellowship Trained Surgeons.

Colour scheme should fit the logo design and be within the general colour recommendations of a medical clinic.

The design should be modern, eye catching, draws the end user to the website.

We would like to design our facebook page for future social media marketing.
In accordance with local advertisement regulations pertaining to medical clinics, no statements must have any information or laudatory statements such as the use of best, better, breakthrough, champions, or any statements that imply superiority and that may create unjustified expectations of services.

Target Market(s)

Patients
Friends family and relatives of patients.

Font styles to use
Serif
Sans Serif

Requirements
Must have
• My project must have my logo.

A nice colour scheme comfortable to the eye.
Nice to have
• Nice eye catching design that will draw the end user to the page.
Should not have
• Must not have any information that create unjustified expectaions.
Must not contain laudatory statements such as best, better, breakthrough, champions, or other statement that may create unjustified expecation of services.

```html
<!DOCTYPE html>
<html lang="en">
<head>
<meta charset="utf-8">
<title>Larchmont Orthopaedics – Page Cover</title>
<link href="https://fonts.googleapis.com/css2?family=Exo+2:wght@600;700&family=Roboto:wght@500&display=swap" rel="stylesheet">
<style>
  :root {
    --bg-dark: #0c2c31;
    --bg-mid: #143d43;
    --accent-teal: #3ccfc5;
    --accent-blue: #1f8ea8;
    --ring-teal: #3f9c9a;
    --panel: #eef7f9;
    --panel-line: #c9dfe5;
    --text-light: #ffffff;
    --text-dark: #1c2e35;
    --tick: #9fb5b8;
    --logo-box: #ffffff;
    --logo-text: #4a5560;
  }
  * { margin: 0; padding: 0; box-sizing: border-box; }
  html, body { width: 1200px; height: 457px; overflow: hidden; background: var(--bg-dark); }
  .cover {
    position: relative;
    width: 1200px;
    height: 457px;
    background: linear-gradient(120deg, var(--bg-mid) 0%, var(--bg-dark) 55%, #0a2529 100%);
    overflow: hidden;
    font-family: "Roboto", Arial, sans-serif;
  }
  .brand {
    position: absolute;
    left: 51px; top: 0;
    width: 325px; height: 88px;
    background: var(--logo-box);
    border-radius: 0 0 10px 10px;
    display: flex; align-items: center; gap: 14px;
    padding-left: 22px;
  }
  .brand-mark {
    width: 42px; height: 42px;
    border-radius: 50%;
    background: var(--ring-teal);
    flex: none;
  }
  .brand-name {
    font-family: "Exo 2", Arial, sans-serif;
    font-weight: 700;
    font-size: 25px;
    line-height: 1.05;
    color: var(--logo-text);
  }
  .services {
    position: absolute;
    left: 38px; top: 120px;
  }
  .section-title {
    font-family: "Exo 2", Arial, sans-serif;
    font-weight: 600;
    font-size: 37px;
    line-height: 52px;
    color: var(--accent-teal);
    margin-bottom: 8px;
  }
  .service-list { list-style: none; }
  .service-list li {
    display: flex; align-items: center; gap: 24px;
    font-weight: 500;
    font-size: 26px;
    color: var(--text-light);
    height: 61px;
  }
  .service-list svg { width: 22px; height: 22px; flex: none; }
  .panel {
    position: absolute;
    left: 487px; top: 18px;
    width: 691px; height: 421px;
    background: var(--panel);
    border-radius: 42px;
  }
  .photo-ring {
    position: absolute;
    left: 410px; top: 92px;
    width: 268px; height: 268px;
    border-radius: 50%;
    background: var(--ring-teal);
    box-shadow: 0 0 0 6px rgba(255,255,255,0.35);
    padding: 11px;
  }
  .photo {
    width: 100%; height: 100%;
    border-radius: 50%;
    background: linear-gradient(90deg, #1f6fc4 0%, #3a8ee0 35%, #6a3a3e 52%, #b3675a 72%, #5a2c2a 100%);
  }
  .usp {
    position: absolute;
    left: 770px; top: 66px;
  }
  .usp-title {
    font-family: "Exo 2", Arial, sans-serif;
    font-weight: 700;
    font-size: 37px;
    line-height: 48px;
    color: var(--accent-blue);
    padding-bottom: 18px;
    border-bottom: 2px solid var(--panel-line);
    width: 344px;
    margin-bottom: 32px;
  }
  .usp-list { list-style: none; }
  .usp-list li {
    display: flex; align-items: flex-start; gap: 18px;
    font-weight: 500;
    font-size: 32px;
    line-height: 41px;
    color: var(--text-dark);
    margin-bottom: 21px;
  }
  .usp-list svg { width: 26px; height: 26px; flex: none; margin-top: 7px; }
</style>
</head>
<body>
<div class="cover">
  <div class="brand">
    <span class="brand-mark"></span>
    <span class="brand-name">Larchmont<br>Orthopaedics</span>
  </div>

  <section class="services">
    <h2 class="section-title">Service We Offer</h2>
    <ul class="service-list">
      <li><svg viewBox="0 0 24 24"><circle cx="12" cy="12" r="10" fill="none" stroke="var(--tick)" stroke-width="1.8"/><path d="M7.5 12.3l3 3 6-6.5" fill="none" stroke="var(--tick)" stroke-width="2" stroke-linecap="round" stroke-linejoin="round"/></svg>Total Knee Replacements</li>
      <li><svg viewBox="0 0 24 24"><circle cx="12" cy="12" r="10" fill="none" stroke="var(--tick)" stroke-width="1.8"/><path d="M7.5 12.3l3 3 6-6.5" fill="none" stroke="var(--tick)" stroke-width="2" stroke-linecap="round" stroke-linejoin="round"/></svg>Total Hip Replacements</li>
      <li><svg viewBox="0 0 24 24"><circle cx="12" cy="12" r="10" fill="none" stroke="var(--tick)" stroke-width="1.8"/><path d="M7.5 12.3l3 3 6-6.5" fill="none" stroke="var(--tick)" stroke-width="2" stroke-linecap="round" stroke-linejoin="round"/></svg>Hip Fractures</li>
      <li><svg viewBox="0 0 24 24"><circle cx="12" cy="12" r="10" fill="none" stroke="var(--tick)" stroke-width="1.8"/><path d="M7.5 12.3l3 3 6-6.5" fill="none" stroke="var(--tick)" stroke-width="2" stroke-linecap="round" stroke-linejoin="round"/></svg>Sports injury of the knee</li>
    </ul>
  </section>

  <div class="panel"></div>

  <div class="photo-ring">
    <div class="photo" role="img" aria-label="Medical imagery of a hip joint and a knee joint highlighted in red"></div>
  </div>

  <section class="usp">
    <h2 class="usp-title">Our Unique Service</h2>
    <ul class="usp-list">
      <li><svg viewBox="0 0 24 24"><circle cx="12" cy="12" r="9.5" fill="none" stroke="var(--accent-blue)" stroke-width="2"/><circle cx="12" cy="12" r="5" fill="var(--accent-blue)"/></svg>Patient Centred Care</li>
      <li><svg viewBox="0 0 24 24"><circle cx="12" cy="12" r="9.5" fill="none" stroke="var(--accent-blue)" stroke-width="2"/><circle cx="12" cy="12" r="5" fill="var(--accent-blue)"/></svg>Value Driven</li>
      <li><svg viewBox="0 0 24 24"><circle cx="12" cy="12" r="9.5" fill="none" stroke="var(--accent-blue)" stroke-width="2"/><circle cx="12" cy="12" r="5" fill="var(--accent-blue)"/></svg>2 Double-Fellowship<br>Trained Surgeons</li>
    </ul>
  </section>
</div>
</body>
</html>
```